International wholesale business needs a business card

We need a business card.

Company Details:
Company Name and logo
Address, Phone number, Website
Employee Details:
Name, Designation, Mobile Number & Email address

```html
<!DOCTYPE html>
<html lang="en">
<head>
<meta charset="utf-8">
<title>Korvel Trading – Business Card</title>
<link rel="stylesheet" href="https://fonts.googleapis.com/css2?family=Open+Sans:wght@400;600;700&display=swap">
<style>
  :root {
    --brand-red: #c1272d;
    --card-white: #ffffff;
    --text-grey: #555555;
    --backdrop: #d9d9d6;
  }
  * { box-sizing: border-box; margin: 0; padding: 0; }
  html, body { width: 1200px; height: 801px; overflow: hidden; }
  body {
    background: var(--backdrop);
    font-family: "Open Sans", Arial, sans-serif;
    display: flex;
    align-items: center;
    justify-content: center;
    gap: 40px;
  }
  .card {
    width: 540px;
    height: 309px;
    position: relative;
    box-shadow: 0 6px 18px rgba(0,0,0,0.18);
  }
  .card-front { background: var(--card-white); border-bottom: 3px solid var(--brand-red); }
  .card-back { background: var(--brand-red); display: flex; align-items: center; justify-content: center; }

  .brand { display: flex; align-items: center; gap: 10px; }
  .brand-dot { border-radius: 50%; flex: none; }
  .brand-name { font-weight: 600; line-height: 1; letter-spacing: 1px; white-space: nowrap; }

  .card-front .brand { position: absolute; left: 30px; top: 150px; max-width: 236px; }
  .card-front .brand-dot { width: 28px; height: 28px; background: var(--brand-red); }
  .card-front .brand-name { color: var(--brand-red); font-size: 19px; }

  .card-back .brand-dot { width: 64px; height: 64px; background: var(--card-white); }
  .card-back .brand-name { color: var(--card-white); font-size: 44px; }

  .divider {
    position: absolute; left: 282px; top: 40px;
    width: 1.5px; height: 229px; background: var(--brand-red);
  }
  .contact { position: absolute; left: 302px; top: 46px; color: var(--text-grey); font-size: 13px; line-height: 1.45; }
  .person-name { color: var(--brand-red); font-weight: 700; font-size: 19px; letter-spacing: 0.3px; }
  .person-title { font-size: 14px; margin-bottom: 14px; }
  .address { margin-bottom: 12px; }
  .contact-list { list-style: none; }
  .contact-list li { display: flex; align-items: center; gap: 8px; }
  .contact-list svg { width: 11px; height: 11px; flex: none; }
</style>
</head>
<body>
  <section class="card card-front">
    <div class="brand">
      <span class="brand-dot"></span>
      <span class="brand-name">KORVEL TRADING</span>
    </div>
    <div class="divider"></div>
    <div class="contact">
      <p class="person-name">DANIEL REYES</p>
      <p class="person-title">President</p>
      <p class="address">1870 Harbor View Dr<br>Seaview CA 90417</p>
      <ul class="contact-list">
        <li>
          <svg viewBox="0 0 12 12" aria-hidden="true"><path fill="#c1272d" d="M2.5 1l2 2-1 1.3c.7 1.5 1.7 2.5 3.2 3.2L8 6.5l2 2-1.3 1.8C5 10 2 7 1.7 3.3z"/></svg>
          <span>555-310-4827</span>
        </li>
        <li>
          <svg viewBox="0 0 12 12" aria-hidden="true"><rect x="3" y="0.8" width="6" height="10.4" rx="1" fill="none" stroke="#c1272d" stroke-width="1.2"/></svg>
          <span>555-310-4827</span>
        </li>
        <li>
          <svg viewBox="0 0 12 12" aria-hidden="true"><rect x="1" y="2.5" width="10" height="7" fill="#c1272d"/><path d="M1 2.5l5 4 5-4" fill="none" stroke="#fff" stroke-width="1"/></svg>
          <span>dreyes@korveltrading.com</span>
        </li>
        <li>
          <svg viewBox="0 0 12 12" aria-hidden="true"><circle cx="6" cy="6" r="5" fill="#c1272d"/><path d="M1 6h10M6 1c-2.5 3-2.5 7 0 10M6 1c2.5 3 2.5 7 0 10" fill="none" stroke="#fff" stroke-width="0.8"/></svg>
          <span>www.korveltrading.com</span>
        </li>
      </ul>
    </div>
  </section>

  <section class="card card-back">
    <div class="brand">
      <span class="brand-dot"></span>
      <span class="brand-name">KORVEL TRADING</span>
    </div>
  </section>
</body>
</html>
```